Medical Practice Business Card

we need a business card for our new medical ophthalmology practice based in Needham Massachusetts. we are looking for a simple , modern and elegant design.
the card needs to contain the following
1- the logo of our practice (please see attached file)
2- the name of the practice : "Silver Birch Retina Care"
3- Doctor's Name: Tobias Rendell MD PhD
4- Specialty: Board-Certified Vitreoretinal Surgeon
5- practice address: 87 Larkspur Ave, Suite 210, Needham MA 02481
7- Office number: 617- 482 - 7730
8- fax number: 617- 391 - 2268
9- email: info@sbretinahub.example
10- website: www.sbretinahub.example

```html
<!DOCTYPE html>
<html lang="en">
<head>
<meta charset="utf-8">
<title>Silver Birch Retina Care – Business Card</title>
<link rel="stylesheet" href="https://fonts.googleapis.com/css2?family=Lora:ital,wght@0,400;0,600;1,400&display=swap">
<style>
  :root {
    --page: #efeee9;
    --navy: #14305f;
    --accent: #2f8fc0;
    --gold: #c9a24a;
    --gold-soft: #e8dcb8;
    --cream: #f3efe4;
    --ice: #d6ebf5;
    --white: #ffffff;
  }
  * { box-sizing: border-box; margin: 0; padding: 0; }
  html, body {
    width: 1055px; height: 1200px; overflow: hidden;
    background: var(--page);
    font-family: "Lora", Georgia, serif;
    color: var(--navy);
  }
  .canvas { position: relative; width: 1055px; height: 1200px; }
  .card {
    position: absolute; left: 225px; width: 606px; height: 392px;
    overflow: hidden; background: var(--white);
    box-shadow: 0 6px 18px rgba(0,0,0,0.12);
  }
  .card--front { top: 118px; }
  .card--back { top: 635px; }

  .front-artwork {
    position: absolute; inset: 0;
    background:
      radial-gradient(ellipse 44% 62% at 60% 50%, var(--white) 55%, rgba(255,255,255,0) 100%),
      radial-gradient(circle at 10% 30%, var(--ice) 0%, rgba(214,235,245,0) 30%),
      radial-gradient(circle at 92% 78%, var(--ice) 0%, rgba(214,235,245,0) 28%),
      linear-gradient(135deg, var(--gold-soft) 0%, var(--cream) 40%, var(--white) 60%, var(--cream) 85%, var(--gold-soft) 100%);
  }
  .back-artwork {
    position: absolute; top: 0; right: 0; width: 300px; height: 100%;
    background:
      radial-gradient(circle at 70% 20%, var(--ice) 0%, rgba(214,235,245,0) 35%),
      linear-gradient(100deg, rgba(255,255,255,1) 0%, rgba(243,239,228,0.7) 40%, var(--cream) 70%, var(--gold-soft) 100%);
  }

  .brand { position: absolute; display: flex; align-items: center; }
  .brand__ring { flex: none; border-radius: 50%; border: 3px solid var(--navy); }
  .brand__name {
    font-weight: 600; color: var(--navy); line-height: 1.08;
    text-transform: uppercase; letter-spacing: 0.5px; white-space: nowrap;
  }
  .card--front .brand { left: 132px; top: 158px; gap: 16px; }
  .card--front .brand__ring { width: 60px; height: 60px; }
  .card--front .brand__name { font-size: 31px; }
  .card--back .brand { left: 44px; top: 62px; gap: 12px; }
  .card--back .brand__ring { width: 40px; height: 40px; }
  .card--back .brand__name { font-size: 22px; }

  .doctor { position: absolute; left: 56px; top: 166px; }
  .doctor__name { font-size: 22px; font-weight: 400; }
  .doctor__title { font-size: 14px; font-style: italic; margin-top: 2px; }

  .contact { position: absolute; left: 54px; top: 246px; width: 500px; }
  .contact__row { display: flex; align-items: flex-start; margin-bottom: 10px; }
  .contact__item { display: flex; align-items: flex-start; gap: 12px; width: 236px; }
  .contact__item--wide { width: 500px; }
  .contact__icon { flex: none; width: 24px; height: 24px; color: var(--accent); }
  .contact__value { font-size: 15.5px; line-height: 1.2; white-space: nowrap; }
  .contact__label { font-size: 11px; font-style: italic; display: block; }
</style>
</head>
<body>
<main class="canvas">

  <section class="card card--front" aria-label="Card front">
    <div class="front-artwork" role="img" aria-label="Soft cream and ice-blue background with gold ribbon curves and geometric gold line pattern"></div>
    <div class="brand">
      <span class="brand__ring"></span>
      <span class="brand__name">Silver Birch<br>Retina Care</span>
    </div>
  </section>

  <section class="card card--back" aria-label="Card back">
    <div class="back-artwork" role="img" aria-label="Gold ribbon curve and geometric gold line pattern over cream and ice-blue tones"></div>
    <div class="brand">
      <span class="brand__ring"></span>
      <span class="brand__name">Silver Birch<br>Retina Care</span>
    </div>

    <div class="doctor">
      <h1 class="doctor__name">Dr. Tobias Rendell MD PhD</h1>
      <p class="doctor__title">Board-Certified Vitreoretinal Surgeon</p>
    </div>

    <div class="contact">
      <div class="contact__row">
        <div class="contact__item contact__item--wide">
          <svg class="contact__icon" viewBox="0 0 24 24" fill="none" stroke="currentColor" stroke-width="1.6"><path d="M12 22s7-7.2 7-12.5A7 7 0 0 0 5 9.5C5 14.8 12 22 12 22z"/><circle cx="12" cy="9.5" r="2.6"/></svg>
          <span class="contact__value">87 Larkspur Ave, Suite 210, Needham MA 02481</span>
        </div>
      </div>
      <div class="contact__row">
        <div class="contact__item">
          <svg class="contact__icon" viewBox="0 0 24 24" fill="none" stroke="currentColor" stroke-width="1.6"><path d="M5 3h3.5l1.8 4.5-2.3 1.6a11 11 0 0 0 6 6l1.6-2.3L20 14.6V18a2 2 0 0 1-2 2A16 16 0 0 1 3 5a2 2 0 0 1 2-2z"/><path d="M14.5 3.5a6 6 0 0 1 6 6M14.5 6.5a3 3 0 0 1 3 3"/></svg>
          <span class="contact__value">617- 482 - 7730<span class="contact__label">Office number</span></span>
        </div>
        <div class="contact__item">
          <svg class="contact__icon" viewBox="0 0 24 24" fill="none" stroke="currentColor" stroke-width="1.6"><rect x="3" y="8" width="5" height="13" rx="1"/><path d="M8 9h12v12H8z"/><path d="M10 9V3h7l2 2v4"/><path d="M11 13h2M15 13h2M11 16h2M15 16h2M11 19h6"/></svg>
          <span class="contact__value">617- 391 - 2268<span class="contact__label">Fax number</span></span>
        </div>
      </div>
      <div class="contact__row">
        <div class="contact__item">
          <svg class="contact__icon" viewBox="0 0 24 24" fill="none" stroke="currentColor" stroke-width="1.6"><rect x="3" y="6" width="18" height="13" rx="1.5"/><path d="M3.5 7l8.5 6.5L20.5 7"/></svg>
          <span class="contact__value">info@sbretinahub.example</span>
        </div>
        <div class="contact__item">
          <svg class="contact__icon" viewBox="0 0 24 24" fill="none" stroke="currentColor" stroke-width="1.6"><circle cx="12" cy="12" r="9"/><path d="M3 12h18M12 3c3 3 3 15 0 18M12 3c-3 3-3 15 0 18M5 7.5h14M5 16.5h14"/></svg>
          <span class="contact__value">www.sbretinahub.example</span>
        </div>
      </div>
    </div>
  </section>

</main>
</body>
</html>
```